Yacht, Boats, Watersports company needs a redesign of business card

Hello Designers!
We are a Boat dealership company that sells fun in the water, we sell boats, Yachts, Kayaks and also yacht WaterSport toys. We are looking to redesign our business cards in to something a little bit more sophisticated. in a way that we can make better use of our company colors. I'm attaching a zipped file containing the company 3 sets of company logo which one is an horizontal another one is a vertical and also a chromed 3d logo. Also is included two set of business cards that we use and also some designs that i think it's interesting. We use PMS 2026c Orange and PMS 7687C Blue. I would like to see at least two different options with the orange as accent and also using blue as an accent color. It's really important for the business cards to have a font option and size that is legible to most people. Our current website is wwww.corvellamarine.com. Please visit if you want to have a better feeling of the Boat dealership
You can send Single sided or double side options. We are now using single sided but we may be open for a double side option if we really like the design.
Target Market(s)
Marine, boat sales, yacht sales, water toys sales/
Contact Information for Business Card
Name: Dale Pritchett
Address: 718 West Halden Lane,
Dania Beach, FL 33019
Phone: 954-382-7146
Fax: 954:382-7139
Cell: 954-451-8320
Email: 212@corvellamarine.com
Website: corvellamarine.com
Requirements
Must have
- the current information of the business card provided.
logo
use the PMS Colors
Nice to have
- a touch of elegance and sophistication but simple
Should not have
- should not have any typography that is hard to read, the card should be simple but yet sophisticated.

```html
<!DOCTYPE html>
<html lang="en">
<head>
<meta charset="utf-8">
<title>Corvella Marine – Business Card</title>
<link href="https://fonts.googleapis.com/css2?family=Open+Sans:wght@400;700&family=Roboto:wght@400&display=swap" rel="stylesheet">
<style>
  :root {
    --blue: #0c58a6;
    --navy: #12467a;
    --orange: #f37124;
    --white: #ffffff;
    --ink: #111111;
  }
  * { margin: 0; padding: 0; box-sizing: border-box; }
  html, body { width: 1200px; height: 1200px; overflow: hidden; background: var(--white); }
  .canvas {
    position: relative; width: 1200px; height: 1200px;
    border: 1px solid var(--ink); background: var(--white);
    font-family: "Open Sans", sans-serif;
  }
  .card { position: absolute; left: 278px; width: 691px; height: 398px; overflow: hidden; }
  .card-front { top: 144px; background: var(--white); border: 1.5px solid var(--ink); }
  .card-back { top: 639px; background: var(--blue); }
  .band { position: absolute; left: 0; top: 0; width: 100%; height: 100%; }
  .brand-name {
    position: absolute; left: 0; right: 0; top: 160px;
    text-align: center; font-weight: 700; font-size: 34px;
    letter-spacing: 3px; color: var(--navy);
  }
  .brand-dot {
    position: absolute; left: 321px; top: 88px; width: 48px; height: 48px;
    border-radius: 50%; background: var(--orange);
  }
  .website {
    position: absolute; left: 0; right: 0; top: 352px;
    display: flex; justify-content: center; align-items: center; gap: 5px;
    color: var(--white); font-size: 16.5px;
  }
  .website svg { width: 13px; height: 13px; }
  .person-name {
    position: absolute; left: 95px; top: 180px;
    font-family: "Roboto", Arial, sans-serif; font-size: 31px; color: var(--white);
  }
  .contact { position: absolute; left: 386px; top: 107px; color: var(--white); font-size: 16px; line-height: 20.5px; }
  .contact-row { position: relative; padding-left: 31px; }
  .contact-row svg { position: absolute; left: 0; top: 3px; width: 14px; height: 14px; }
  .row-address { margin-bottom: 11px; }
  .row-phone { margin-bottom: 7px; }
  .row-fax { margin-bottom: 9px; }
  .row-cell { margin-bottom: 9px; }
</style>
</head>
<body>
<div class="canvas">

  <section class="card card-front">
    <div class="brand-dot"></div>
    <div class="brand-name">CORVELLA MARINE</div>
    <svg class="band" viewBox="0 0 691 398" preserveAspectRatio="none">
      <polygon fill="var(--blue)" points="0,329 312,329 339,308 366,329 691,329 691,398 0,398"/>
    </svg>
    <div class="website">
      <svg viewBox="0 0 14 14" fill="none" stroke="#fff" stroke-width="1.2"><circle cx="7" cy="7" r="5.8"/><ellipse cx="7" cy="7" rx="2.6" ry="5.8"/><line x1="1.2" y1="7" x2="12.8" y2="7"/></svg>
      <span>corvellamarine.com</span>
    </div>
  </section>

  <section class="card card-back">
    <svg class="band" viewBox="0 0 691 398" preserveAspectRatio="none">
      <polygon fill="var(--orange)" points="0,331 312,331 339,310 366,331 691,331 691,398 0,398"/>
    </svg>
    <div class="person-name">Dale Pritchett</div>
    <div class="contact">
      <div class="contact-row row-address">
        <svg viewBox="0 0 14 14" fill="none" stroke="#fff" stroke-width="1.2"><path d="M7 13 C3 8.5 2.5 7 2.5 5.5 A4.5 4.5 0 0 1 11.5 5.5 C11.5 7 11 8.5 7 13Z"/><circle cx="7" cy="5.5" r="1.5"/></svg>
        Address: 718 West Halden Lane,<br>Dania Beach, FL 33019
      </div>
      <div class="contact-row row-phone">
        <svg viewBox="0 0 14 14" fill="none" stroke="#fff" stroke-width="1.2"><path d="M3 1.5 L5 1.5 L6 4.5 L4.6 5.6 C5.4 7.4 6.6 8.6 8.4 9.4 L9.5 8 L12.5 9 L12.5 11 C12.5 12 11.5 12.5 10.5 12.5 C5.5 12 2 8.5 1.5 3.5 C1.5 2.5 2 1.5 3 1.5Z"/></svg>
        954-382-7146
      </div>
      <div class="contact-row row-fax">Fax: 954:382-7139</div>
      <div class="contact-row row-cell">
        <svg viewBox="0 0 14 14" fill="none" stroke="#fff" stroke-width="1.1"><rect x="3.5" y="0.6" width="7" height="12.8" rx="0.8"/><line x1="6.3" y1="12" x2="7.7" y2="12"/></svg>
        954-451-8320
      </div>
      <div class="contact-row row-email">
        <svg viewBox="0 0 14 14" fill="none" stroke="#fff" stroke-width="1.1"><circle cx="7" cy="7" r="5.5"/><circle cx="7" cy="7" r="2"/><path d="M9 7 V8 A1.5 1.5 0 0 0 12 8"/></svg>
        212@corvellamarine.com
      </div>
    </div>
  </section>

</div>
</body>
</html>
```